Clear Plastic Card Design

I am looking to have a business card designed from my logo icon. I am looking to match the style of a different business card I have attached in the files.
Looking for a card that is plastic, with layers of transparency in the shape of my logo icon (also attached in the files) - not a circle like the other card. The winning design will incorporate the red icon logo on the front and back and include the charity's name, "Lanterns for the Weary" in the same or similar font, as well as an email and phone number. For now, use the email: email@lanternsfortheweary.org and the phone number 555-318-4072.
We like how the sample business card has transparency, partial and full opacity layers and a matching color scheme. Files will need to be in vector so that our business card printing company can work with it.
UPDATE:
We've some excellent designs in, thank you everyone! I got an early review from the owner, and he requested a minor redirect to find his perfect design. He wants the design to stand out by NOT being a rectangle. Try instead a circle, square, or best yet - something that falls in the outline of the logo icon, either fully or partially. Thank you, everyone!
Contact Information for Business Card
Lanterns for the Weary text should be incorporated as well as a phone and email.
Look and feel

```html
<!DOCTYPE html>
<html lang="en">
<head>
<meta charset="utf-8">
<title>Lanterns for the Weary – Business Card</title>
<link rel="stylesheet" href="https://fonts.googleapis.com/css2?family=Arimo:wght@400&family=Lexend:wght@400&display=swap">
<style>
  :root {
    --backdrop: #616161;
    --card-grey: #707070;
    --card-white: #ffffff;
    --accent: #d9532a;
    --ink: #111111;
  }
  html, body {
    margin: 0;
    padding: 0;
    width: 1200px;
    height: 781px;
    overflow: hidden;
    background: var(--backdrop);
  }
  .card {
    position: absolute;
    left: 122px;
    top: 99px;
    width: 1001px;
    height: 572px;
    border-radius: 46px;
    background: var(--card-grey);
    overflow: hidden;
  }
  .card__wave {
    position: absolute;
    inset: 0;
    width: 1001px;
    height: 572px;
  }
  .card__edge {
    position: absolute;
    top: 119px;
    width: 10px;
    height: 333px;
    background: var(--accent);
  }
  .card__edge--left { left: 0; }
  .card__edge--right { right: 0; }

  .brand__mark {
    position: absolute;
    left: 752px;
    top: 70px;
    width: 210px;
    height: 210px;
    background: var(--accent);
  }
  .brand__name {
    position: absolute;
    right: 270px;
    top: 214px;
    margin: 0;
    font-family: "Lexend", sans-serif;
    font-weight: 400;
    font-size: 46px;
    line-height: 50px;
    color: var(--ink);
    text-align: right;
    letter-spacing: -0.5px;
  }

  .contact {
    position: absolute;
    left: 50px;
    top: 391px;
    margin: 0;
    padding: 0;
    list-style: none;
    font-family: "Arimo", sans-serif;
    font-size: 31px;
    color: var(--ink);
  }
  .contact__item {
    display: flex;
    align-items: center;
    height: 40px;
    margin-bottom: 8px;
  }
  .contact__icon {
    width: 40px;
    height: 40px;
    margin-right: 18px;
    flex: none;
  }
  .website {
    position: absolute;
    left: 248px;
    top: 514px;
    margin: 0;
    font-family: "Arimo", sans-serif;
    font-size: 32px;
    color: var(--accent);
  }
</style>
</head>
<body>
  <div class="card">
    <svg class="card__wave" viewBox="0 0 1001 572" aria-hidden="true">
      <path d="M0,336 C150,305 330,330 520,370 C700,410 880,425 1001,400 L1001,572 L0,572 Z" fill="var(--card-white)"/>
    </svg>
    <div class="card__edge card__edge--left"></div>
    <div class="card__edge card__edge--right"></div>

    <div class="brand__mark" aria-hidden="true"></div>
    <p class="brand__name">Lanterns for<br>the Weary</p>

    <ul class="contact">
      <li class="contact__item">
        <svg class="contact__icon" viewBox="0 0 40 40" aria-hidden="true">
          <circle cx="20" cy="20" r="18.5" fill="none" stroke="var(--ink)" stroke-width="2"/>
          <rect x="13.5" y="9.5" width="13" height="21" rx="2.5" fill="none" stroke="var(--ink)" stroke-width="2"/>
        </svg>
        <span>555-318-4072</span>
      </li>
      <li class="contact__item">
        <svg class="contact__icon" viewBox="0 0 40 40" aria-hidden="true">
          <circle cx="20" cy="20" r="18.5" fill="none" stroke="var(--ink)" stroke-width="2"/>
          <rect x="9" y="13" width="22" height="15" rx="2" fill="var(--ink)"/>
          <path d="M10 14 L20 21.5 L30 14" fill="none" stroke="var(--card-white)" stroke-width="1.6"/>
        </svg>
        <span>email@lanternsfortheweary.org</span>
      </li>
    </ul>

    <p class="website">www. lanternsfortheweary.org</p>
  </div>
</body>
</html>
```